Patient Satisfaction

We are extending our social listening and intelligence platform for Physicians to patient satisfaction app. Our platform monitors social media and review sites and collects, classifies and distilled patient satisfaction into nine Categories - Thoroughness, Answers Q's, Collaborative, Caring, Time Spent, Previous Success, Instruction Clarity, Follow-up and Reputation

The app will have three main states: (1) Home state showing the metric for each category, (2) a detailed page for each Category showing the metric, topics discussed and sites sourced, (3) Leaderboard showing Physicians with best scores.

If you follow our wireframes, please take liberty to extend it. We like the Lumora 6 tiles, but our wireframes fall far short of meeting its coolness and usefulness. For example, we don't have different size tiles, and would live them, or content on the tiles to make them more meaningful. [Note: use KT instead of QRM.]
Updates

The designs submitted to date look great, but they reminded me that my instructions were unclear. Feel free to follow the wireframes if you like the UI, but we also welcome your thoughts on UI in addition to look and feel. If you follow our wireframes, please take liberty to extend it. We like the Lumora 6 tile, but our wireframes falls far short of meeting its coolness and usefulness. For example, we don't have different size tiles or content on the tiles to make them more meaningful. If you've submitted designs, please feel free to revise them or submit a different look. And if you haven't submitted designs, please feel free to give us your best thoughts on UI and design.

Target Market(s)

US Physicians

Industry/Entity Type

Media

Font styles to use
Sans Serif

Colors
f37022
5c5c5c
33a6d7

Requirements
Must have
• Home state
Visual icons
Nice to have
• Leaderbaord

```html
<!DOCTYPE html>
<html lang="en">
<head>
<meta charset="utf-8">
<title>Dashboard</title>
<link href="https://fonts.googleapis.com/css2?family=Open+Sans:wght@400;600&display=swap" rel="stylesheet">
<style>
  :root {
    --orange: #fd9a05;
    --blue: #2f9bd0;
    --grid-bg: #4a4a4a;
    --stat-bg: #e4e4e4;
    --stat-text: #555555;
    --white: #ffffff;
  }
  * { margin: 0; padding: 0; box-sizing: border-box; }
  html, body { width: 676px; height: 1200px; overflow: hidden; }
  body { font-family: "Open Sans", Arial, sans-serif; background: var(--white); }
  .screen { position: relative; width: 676px; height: 1200px; overflow: hidden; }

  .app-header {
    position: absolute; left: 0; top: 0; width: 676px; height: 137px;
    background: var(--orange); color: var(--white);
  }
  .menu-button { position: absolute; left: 30px; top: 80px; width: 33px; height: 19px; }
  .app-title {
    position: absolute; left: 0; right: 0; top: 60px; text-align: center;
    font-size: 38px; font-weight: 400; line-height: 1;
  }

  .hero-photo {
    position: absolute; left: 0; top: 137px; width: 676px; height: 433px;
    background: linear-gradient(100deg, #f1eeea 0%, #e9e4df 35%, #dfe6ec 60%, #eef2f5 100%);
  }
  .score-badge {
    position: absolute; left: 387px; top: 374px; width: 289px; height: 167px;
    background: var(--orange); color: var(--white);
  }
  .score-badge .score-label { position: absolute; left: 15px; top: 104px; font-size: 42px; line-height: 1; }
  .score-badge .score-value { position: absolute; left: 52px; top: -10px; font-size: 172px; line-height: 1; font-weight: 400; letter-spacing: -4px; }

  .stats-bar {
    position: absolute; left: 0; top: 570px; width: 676px; height: 111px;
    background: var(--stat-bg); color: var(--stat-text); font-size: 34px;
  }
  .stat { position: absolute; top: 36px; display: flex; align-items: center; line-height: 1; }
  .stat svg { margin-right: 12px; }
  .stat strong { font-weight: 600; margin-left: 8px; }
  .stat-rank { left: 50px; }
  .stat-comments { left: 363px; }

  .tile-grid { position: absolute; left: 0; top: 681px; width: 676px; height: 519px; background: var(--grid-bg); }
  .tile { position: absolute; color: var(--white); }
  .tile-blue { background: var(--blue); }
  .tile-orange { background: var(--orange); }
  .tile-label { position: absolute; left: 14px; bottom: 8px; font-size: 24px; line-height: 1.3; }
  .tile svg { position: absolute; }

  .tile-bedside { left: 11px; top: 12px; width: 156px; height: 153px; }
  .tile-outcome { left: 176px; top: 12px; width: 158px; height: 153px; }
  .tile-communication { left: 343px; top: 12px; width: 325px; height: 335px; }
  .tile-time { left: 11px; top: 176px; width: 323px; height: 333px; }
  .tile-knowledge { left: 343px; top: 357px; width: 325px; height: 152px; }
  .tile-time .tile-label, .tile-knowledge .tile-label, .tile-communication .tile-label { left: 18px; bottom: 12px; font-size: 25px; }
</style>
</head>
<body>
<div class="screen">
  <header class="app-header">
    <svg class="menu-button" viewBox="0 0 33 19" aria-hidden="true">
      <rect y="0" width="33" height="3" fill="#fff"/>
      <rect y="8" width="33" height="3" fill="#fff"/>
      <rect y="16" width="33" height="3" fill="#fff"/>
    </svg>
    <h1 class="app-title">Dashboard</h1>
  </header>

  <div class="hero-photo" role="img" aria-label="Photo of a smiling physician with a stethoscope and clipboard in a bright clinic, patients in the background"></div>

  <div class="score-badge">
    <span class="score-label">KT</span>
    <span class="score-value">72</span>
  </div>

  <section class="stats-bar">
    <div class="stat stat-rank">
      <svg width="38" height="40" viewBox="0 0 38 40" aria-hidden="true">
        <path d="M4 2 L8 2 L13 38 L9 38 Z" fill="#555"/>
        <path d="M7 4 C15 0 22 8 35 4 L31 20 C20 24 14 16 9 20 Z" fill="#555"/>
      </svg>
      <span>Rank:<strong>5/15</strong></span>
    </div>
    <div class="stat stat-comments">
      <svg width="42" height="40" viewBox="0 0 42 40" aria-hidden="true">
        <ellipse cx="22" cy="18" rx="19" ry="17" fill="#555"/>
        <path d="M6 26 L3 38 L15 31 Z" fill="#555"/>
      </svg>
      <span>Comment:<strong>22</strong></span>
    </div>
  </section>

  <section class="tile-grid">
    <div class="tile tile-blue tile-bedside">
      <svg style="left:34px;top:14px" width="84" height="58" viewBox="0 0 84 58" aria-hidden="true">
        <circle cx="12" cy="10" r="7" fill="#fff"/>
        <path d="M18 12 L60 26 L57 33 L16 21 Z" fill="#fff"/>
        <path d="M6 24 L62 38 L80 30 L84 34 L63 46 L4 31 Z" fill="#fff"/>
        <rect x="36" y="40" width="7" height="14" fill="#fff"/>
        <rect x="26" y="52" width="28" height="5" fill="#fff"/>
      </svg>
      <span class="tile-label">Bedside</span>
    </div>
    <div class="tile tile-orange tile-outcome">
      <svg style="left:48px;top:44px" width="60" height="54" viewBox="0 0 60 54" aria-hidden="true">
        <path d="M30 52 L6 28 C-4 18 2 2 16 2 C23 2 27 6 30 10 C33 6 37 2 44 2 C58 2 64 18 54 28 Z" fill="#fff"/>
        <path d="M6 27 L20 27 L25 17 L31 37 L36 22 L40 27 L54 27" fill="none" stroke="#fd9a05" stroke-width="3.5" stroke-linejoin="round"/>
      </svg>
      <span class="tile-label">Outcome</span>
    </div>
    <div class="tile tile-blue tile-communication">
      <svg style="left:107px;top:101px" width="100" height="100" viewBox="0 0 100 100" aria-hidden="true">
        <circle cx="52" cy="46" r="46" fill="#fff"/>
        <path d="M14 66 L6 100 L40 84 Z" fill="#fff"/>
      </svg>
      <span class="tile-label">Communication</span>
    </div>
    <div class="tile tile-blue tile-time">
      <svg style="left:99px;top:86px" width="118" height="118" viewBox="0 0 118 118" aria-hidden="true">
        <circle cx="59" cy="59" r="54" fill="none" stroke="#fff" stroke-width="6"/>
        <path d="M55 26 L55 63 L79 85" fill="none" stroke="#fff" stroke-width="6" stroke-linecap="round" stroke-linejoin="round"/>
      </svg>
      <span class="tile-label">Time Spent</span>
    </div>
    <div class="tile tile-orange tile-knowledge">
      <svg style="left:124px;top:21px" width="70" height="66" viewBox="0 0 70 66" aria-hidden="true">
        <path d="M3 6 C14 2 24 4 35 10 C46 4 56 2 67 6 L67 60 C56 56 46 58 35 64 C24 58 14 56 3 60 Z" fill="none" stroke="#fff" stroke-width="5" stroke-linejoin="round"/>
        <line x1="35" y1="10" x2="35" y2="64" stroke="#fff" stroke-width="4"/>
        <g stroke="#fff" stroke-width="4">
          <line x1="11" y1="20" x2="27" y2="22"/><line x1="11" y1="31" x2="27" y2="33"/><line x1="11" y1="42" x2="27" y2="44"/>
          <line x1="43" y1="22" x2="59" y2="20"/><line x1="43" y1="33" x2="59" y2="31"/><line x1="43" y1="44" x2="59" y2="42"/>
        </g>
      </svg>
      <span class="tile-label">Knowlegde</span>
    </div>
  </section>
</div>
</body>
</html>
```